New Website design 2024: Ridgeline Flameguard, Inc.

1. Who we are: At Ridgeline Flameguard Inc, our mission is to provide our clients with comprehensive firestop and seismic expansion joint solutions that ensure the safety and integrity of their buildings. We specialize in the installation of firestop systems at penetrations, wall joints, and slab edge joints, as well as providing acoustical sealants, security sealants, architectural caulking, and seismic expansion joints. Since our establishment in 2007, we have been committed to improving the safety and integrity of buildings through our expertise and use of tested and approved firestop systems. Our focus is to deliver exceptional service and quality workmanship to ensure the protection of lives and property.
2. Services we provide:
-Firestopping: T-ratings, CMU Wall Joint, Exterior Caulking, Fireproof Patching, Head of Wall Joints, Through Penetrations, Curtain Wall/Slab Edge, Grease & Fume Duct Protection.
-Expansion Joints: Floor Covers, Roof Covers, Fire Barriers, Vapor Barriers, Wall & Ceiling Covers, Compression Seals, Pre-Compression Foams, Photoluminescent Signage
3. Examples of scope and projects we’ve completed.
4. How to contact us.: https://ridgelineflameguard.example/contact/
- Social Media Links: https://www.linkedin.example/company/ridgeline-flameguard/mycompany/
https://www.instagram.example/ridgelineflameguard/?hl=en
https://www.youtube.example/channel/UCQ8M2RT5KwpZdNvTeLoJbHs/videos
Target Market(s)
Commercial Construction industry
Industry/Entity Type
Commercial Construction industry in California
Coding
Coded - Design and coding required
Number of Pages Required
4 page
Colors
Designer to choose colors to be used in the design.
Requirements
Must have
- 1. Who we are. 2. Services we provide. 3. Examples of scope and projects we’ve completed. 4. How to contact us.
Nice to have
- Logo. Pictures of scope of work and pictures of projects completed or working on.
Should not have
- Names of clients.

```html
<!DOCTYPE html>
<html lang="en">
<head>
<meta charset="utf-8">
<title>Ridgeline Flameguard, Inc.</title>
<link href="https://fonts.googleapis.com/css2?family=Poppins:wght@400;500;600;700;800&display=swap" rel="stylesheet">
<style>
:root{
  --blue:#3a4fa8;
  --blue-dark:#2c3d8c;
  --red:#e0202e;
  --red-dark:#c3121f;
  --ink:#2b2b2b;
  --muted:#555b66;
  --grey:#f2f2f4;
  --white:#ffffff;
}
*{box-sizing:border-box;margin:0;padding:0}
html,body{width:1200px;height:4448px;overflow:hidden}
body{position:relative;font-family:"Poppins",sans-serif;color:var(--ink);background:var(--white)}
a{color:inherit;text-decoration:none}

/* header & hero */
.hero{position:absolute;left:0;top:0;width:1200px;height:660px;overflow:hidden}
.hero-photo{position:absolute;inset:0;background:linear-gradient(135deg,#4d4a48 0%,#77716a 40%,#5c5550 70%,#3b3a3c 100%)}
.hero-shade{position:absolute;inset:0;background:linear-gradient(90deg,rgba(20,22,30,.72) 0%,rgba(20,22,30,.35) 60%,rgba(20,22,30,.2) 100%)}
.nav-bar{position:absolute;left:340px;top:0;width:860px;height:88px;background:var(--blue);clip-path:polygon(40px 0,100% 0,100% 100%,0 100%)}
.brand{position:absolute;left:112px;top:16px;width:240px;height:60px;background:var(--white);display:flex;align-items:center;gap:10px;padding:0 14px}
.brand-mark{width:18px;height:18px;background:var(--red);flex:none}
.brand-name{font-weight:700;font-size:15px;color:var(--red);line-height:1.1;text-transform:uppercase}
.nav-links{position:absolute;left:532px;top:30px;display:flex;gap:44px;font-size:17px;font-weight:500;color:var(--white)}
.nav-cta{position:absolute;left:924px;top:22px;width:156px;height:46px;background:var(--red);color:var(--white);font-size:16px;font-weight:500;display:flex;align-items:center;justify-content:center}
.hero-title{position:absolute;left:172px;top:338px;color:var(--white);font-weight:800;font-size:58px;line-height:62px;text-transform:uppercase}
.hero-tag{position:absolute;left:172px;top:468px;color:var(--white);font-size:16px}
.btn{display:flex;align-items:center;justify-content:center;gap:8px;color:var(--white);font-size:15px;font-weight:600;text-transform:uppercase}
.btn-blue{background:var(--blue)}
.btn-red{background:var(--red)}
.hero-btn1{position:absolute;left:172px;top:500px;width:196px;height:48px}
.hero-btn2{position:absolute;left:388px;top:500px;width:180px;height:48px}
.emblem{position:absolute;left:556px;top:596px;width:88px;height:88px;border-radius:50%;background:var(--white);border:6px solid var(--red);z-index:3}

/* about */
.about{position:absolute;left:0;top:660px;width:1200px;height:760px}
.oct-frame{position:absolute;left:172px;top:168px;width:416px;height:416px;background:var(--blue);clip-path:polygon(29% 0,71% 0,100% 29%,100% 71%,71% 100%,29% 100%,0 71%,0 29%)}
.oct-photo{position:absolute;left:14px;top:14px;width:388px;height:388px;background:linear-gradient(160deg,#b9a58c 0%,#8b7a68 45%,#5b5250 100%);clip-path:polygon(29% 0,71% 0,100% 29%,100% 71%,71% 100%,29% 100%,0 71%,0 29%)}
.exp-badge{position:absolute;left:452px;top:272px;width:108px;height:80px;background:var(--red);color:var(--white);text-align:center;padding-top:6px}
.exp-badge b{display:block;font-size:36px;line-height:40px;font-weight:700}
.exp-badge span{display:block;font-size:13px;line-height:16px;white-space:nowrap}
.about-emblem{position:absolute;left:352px;top:592px;width:56px;height:56px;border-radius:50%;background:var(--white);border:5px solid var(--red)}
.eyebrow{display:flex;align-items:center;gap:10px;color:var(--red);font-weight:600;font-size:16px}
.dot{width:22px;height:22px;border-radius:50%;background:var(--red)}
.about-eyebrow{position:absolute;left:656px;top:156px}
.about-title{position:absolute;left:656px;top:196px;width:480px;font-size:36px;line-height:38px;font-weight:700;color:var(--blue);text-transform:uppercase}
.about-text{position:absolute;left:656px;top:300px;width:482px;font-size:13px;line-height:20.5px;color:var(--muted)}
.about-btn{position:absolute;left:656px;top:548px;width:160px;height:46px}

/* stats */
.stats{position:absolute;left:0;top:1420px;width:1200px;height:620px;background:linear-gradient(160deg,#3a4fa8 0%,#6a3c8e 45%,#d52436 100%)}
.stat{position:absolute;top:192px;width:240px;text-align:center;color:var(--white)}
.stat svg{display:block;margin:0 auto 26px}
.stat b{display:block;font-size:58px;line-height:66px;font-weight:600}
.stat span{font-size:17px}

/* services */
.services{position:absolute;left:0;top:2040px;width:1200px;height:840px}
.sec-head{position:absolute;left:0;width:1200px;text-align:center}
.sec-dot{width:34px;height:34px;border-radius:50%;background:var(--red);margin:0 auto}
.sec-kicker{color:var(--red);font-weight:600;font-size:17px;margin-top:4px}
.sec-title{color:var(--blue);font-weight:700;font-size:38px;margin-top:2px;text-transform:uppercase}
.card{position:absolute;top:240px;width:452px;height:540px;background:var(--grey);text-align:center}
.card-oct{position:absolute;left:116px;top:20px;width:220px;height:220px;background:var(--blue);clip-path:polygon(29% 0,71% 0,100% 29%,100% 71%,71% 100%,29% 100%,0 71%,0 29%)}
.card-oct div{position:absolute;left:9px;top:9px;width:202px;height:202px;clip-path:polygon(29% 0,71% 0,100% 29%,100% 71%,71% 100%,29% 100%,0 71%,0 29%)}
.card-emblem{position:absolute;left:208px;top:222px;width:36px;height:36px;border-radius:50%;background:var(--white);border:4px solid var(--red)}
.card h3{position:absolute;left:0;top:322px;width:100%;font-size:26px;font-weight:700;color:var(--blue);text-transform:uppercase}
.card p{position:absolute;left:40px;top:366px;width:372px;font-size:14px;line-height:22px;color:var(--muted)}
.card .btn{position:absolute;left:146px;top:464px;width:160px;height:44px;text-transform:none;font-weight:500}

/* projects */
.projects-band{position:absolute;left:0;top:2888px;width:1200px;height:330px;background:linear-gradient(200deg,#e2202c 0%,#c12241 45%,#4a4fa4 100%)}
.projects-title{position:absolute;left:0;top:3000px;width:1200px;text-align:center;color:var(--white);font-weight:700;font-size:36px;text-transform:uppercase}
.shots{position:absolute;left:64px;top:3064px;width:1076px;height:228px;display:flex}
.shot{flex:1;height:100%}

/* partners */
.partners{position:absolute;left:80px;top:3510px;width:1040px;display:grid;grid-template-columns:repeat(4,1fr);row-gap:34px;column-gap:80px}
.partner{height:34px;background:#d9dadd}
.partner.dark{background:#3b3b3f}
.partner.redish{background:#d43c3c}

/* contact */
.contact-card{position:absolute;left:180px;top:3760px;width:840px;height:320px;z-index:2;background:linear-gradient(150deg,rgba(200,36,54,.92) 0%,rgba(110,50,130,.92) 55%,rgba(58,79,168,.95) 100%)}
.field{position:absolute;height:30px;border:1px solid rgba(255,255,255,.55);color:rgba(255,255,255,.85);font-size:13px;padding:6px 12px}
.send{position:absolute;left:100px;top:252px;width:640px;height:34px;border:1px solid rgba(255,255,255,.55);color:var(--white);font-size:15px;display:flex;align-items:center;justify-content:center}

/* footer */
.footer{position:absolute;left:0;top:4040px;width:1200px;height:408px;background:var(--blue);color:var(--white)}
.foot-brand{position:absolute;left:120px;top:150px;width:180px;height:46px;background:var(--white);display:flex;align-items:center;gap:8px;padding:0 10px}
.foot-brand .brand-name{font-size:12px}
.foot-text{position:absolute;left:120px;top:208px;width:200px;font-size:14px;line-height:20px}
.foot-col{position:absolute;top:150px}
.foot-col h4{font-size:17px;font-weight:600;margin-bottom:18px;text-transform:uppercase}
.foot-col li{list-style:none;font-size:14px;line-height:28px}
.info{display:flex;align-items:center;gap:12px;font-size:14px;line-height:18px;margin-bottom:16px}
.socials{display:flex;gap:10px}
.socials span{width:30px;height:30px;border-radius:50%;background:var(--white)}
.copy{position:absolute;left:0;top:360px;width:1200px;height:48px;border-top:1px solid rgba(255,255,255,.25);font-size:12px}
.copy span{position:absolute;top:16px}
</style>
</head>
<body>

<header class="hero">
  <div class="hero-photo" role="img" aria-label="Photo of a large commercial construction site interior with steel framing"></div>
  <div class="hero-shade"></div>
  <div class="nav-bar"></div>
  <a class="brand" href="#"><span class="brand-mark"></span><span class="brand-name">Ridgeline Flameguard</span></a>
  <nav class="nav-links"><a href="#">Home</a><a href="#">About</a><a href="#">Services</a><a href="#">Projects</a></nav>
  <a class="nav-cta" href="https://ridgelineflameguard.example/contact/">Contact Us</a>
  <h1 class="hero-title">Ridgeline<br>Flameguard, Inc</h1>
  <p class="hero-tag">Keeping Fire Safety &amp; Structural Integrity</p>
  <a class="btn btn-blue hero-btn1" href="#">Our Projects →</a>
  <a class="btn btn-red hero-btn2" href="#">Contact Us →</a>
</header>
<div class="emblem"></div>

<section class="about">
  <div class="oct-frame"><div class="oct-photo" role="img" aria-label="Photo of a firestopping technician in safety vest and hard hat on site"></div></div>
  <div class="exp-badge"><b>15</b><span>Years Of Experience</span></div>
  <div class="about-emblem"></div>
  <div class="eyebrow about-eyebrow"><span class="dot"></span>Who We Are</div>
  <h2 class="about-title">About Ridgeline Flameguard</h2>
  <p class="about-text">At Ridgeline Flameguard Inc, our mission is to provide our clients with comprehensive firestop and seismic expansion joint solutions that ensure the safety and integrity of their buildings. We specialize in the installation of firestop systems at penetrations, wall joints, and slab edge joints, as well as providing acoustical sealants, security sealants, architectural caulking, and seismic expansion joints. Since our establishment in 2007, we have been committed to improving the safety and integrity of buildings through our expertise and use of tested and approved firestop systems. Our focus is to deliver exceptional service and quality workmanship to ensure the protection of lives and property.</p>
  <a class="btn btn-blue about-btn" href="#">About Us →</a>
</section>

<section class="stats">
  <div class="stat" style="left:72px">
    <svg width="86" height="86" viewBox="0 0 86 86" fill="none" stroke="#fff" stroke-width="2.5"><circle cx="43" cy="43" r="40"/><path d="M28 40h8v20h-8zM36 42l8-14c3 0 4 2 4 5l-1 7h10c3 0 4 3 3 5l-4 12c-1 2-2 3-4 3H36"/></svg>
    <b>15+</b><span>Years of Experience</span>
  </div>
  <div class="stat" style="left:340px">
    <svg width="86" height="86" viewBox="0 0 86 86" fill="none" stroke="#fff" stroke-width="2.5"><circle cx="43" cy="43" r="40"/><circle cx="35" cy="36" r="6"/><circle cx="52" cy="36" r="6"/><path d="M24 58c0-8 5-13 11-13s11 5 11 13M41 58c0-8 5-13 11-13s11 5 11 13"/></svg>
    <b>200+</b><span>Employees</span>
  </div>
  <div class="stat" style="left:612px">
    <svg width="86" height="86" viewBox="0 0 86 86" fill="none" stroke="#fff" stroke-width="2.5"><circle cx="43" cy="43" r="40"/><path d="M32 26h22v10c0 7-5 12-11 12s-11-5-11-12zM32 30h-6c0 6 3 9 7 9M54 30h6c0 6-3 9-7 9M43 48v8M34 60h18"/></svg>
    <b>25+</b><span>Associated Members</span>
  </div>
  <div class="stat" style="left:880px">
    <svg width="86" height="86" viewBox="0 0 86 86" fill="none" stroke="#fff" stroke-width="2.5"><circle cx="43" cy="43" r="40"/><path d="M28 42c0-9 7-15 15-15s15 6 15 15M25 42h36M43 27v8M32 46c2 7 6 10 11 10s9-3 11-10"/></svg>
    <b>100+</b><span>Completed Projects</span>
  </div>
</section>

<section class="services">
  <div class="sec-head" style="top:60px">
    <div class="sec-dot"></div>
    <p class="sec-kicker">Services</p>
    <h2 class="sec-title">Our Quality Services</h2>
  </div>
  <article class="card" style="left:132px">
    <div class="card-oct"><div role="img" aria-label="Photo of a worker installing firestop systems" style="background:linear-gradient(160deg,#9c8a73,#5e5a58)"></div></div>
    <div class="card-emblem"></div>
    <h3>Firestopping</h3>
    <p>Our firestopping systems effectively seal openings and joints in fire-resistance rated walls and floors, ensuring the integrity of the assembly and preventing the spread of fire and smoke.</p>
    <a class="btn btn-blue" href="#">Learn More →</a>
  </article>
  <article class="card" style="left:600px">
    <div class="card-oct"><div role="img" aria-label="Photo of a worker inspecting expansion joints on a deck" style="background:linear-gradient(160deg,#a9b0bb,#6d6660)"></div></div>
    <div class="card-emblem"></div>
    <h3>Expansion Joints</h3>
    <p>Our expansion joints provide essential stress relief on building material, accommodating building movement from seismic events, thermal expansion caused by temperature changes, and wind sway.</p>
    <a class="btn btn-blue" href="#">Learn More →</a>
  </article>
</section>

<section>
  <div class="projects-band"></div>
  <h2 class="projects-title">Our Recent Projects</h2>
  <div class="shots">
    <div class="shot" role="img" aria-label="Photo of a stadium under construction" style="background:linear-gradient(160deg,#b9c3cf,#7d6f64)"></div>
    <div class="shot" role="img" aria-label="Photo of cranes over a building site" style="background:linear-gradient(160deg,#6f8fc4,#5a5550)"></div>
    <div class="shot" role="img" aria-label="Photo of an interior concrete structure in progress" style="background:linear-gradient(160deg,#b8a892,#6e5f55)"></div>
  </div>
</section>

<section class="partners" aria-label="Partners">
  <div class="partner redish"></div><div class="partner dark"></div><div class="partner dark"></div><div class="partner"></div>
  <div class="partner redish"></div><div class="partner dark"></div><div class="partner dark"></div><div class="partner"></div>
</section>

<form class="contact-card">
  <div class="field" style="left:100px;top:36px;width:310px">First Name</div>
  <div class="field" style="left:430px;top:36px;width:310px">Last Name</div>
  <div class="field" style="left:100px;top:84px;width:310px">Email</div>
  <div class="field" style="left:430px;top:84px;width:310px">Phone</div>
  <div class="field" style="left:100px;top:132px;width:640px;height:100px">Message</div>
  <div class="send">Send</div>
</form>

<footer class="footer">
  <div class="foot-brand"><span class="brand-mark"></span><span class="brand-name">Ridgeline Flameguard</span></div>
  <p class="foot-text">We are dedicated to the very best in the provision and installation of firestopping and seismic expansion joints</p>
  <div class="foot-col" style="left:400px">
    <h4>Quick Links</h4>
    <ul><li>Home</li><li>About us</li><li>Projects</li><li>Contact us</li></ul>
  </div>
  <div class="foot-col" style="left:640px">
    <h4>Contact Info</h4>
    <div class="info"><svg width="16" height="16" viewBox="0 0 16 16" fill="#fff"><path d="M8 1a5 5 0 0 0-5 5c0 4 5 9 5 9s5-5 5-9a5 5 0 0 0-5-5zm0 7a2 2 0 1 1 0-4 2 2 0 0 1 0 4z"/></svg><span>1420 Harbor Crest Dr<br>Tustin, CA 92780</span></div>
    <div class="info"><svg width="16" height="16" viewBox="0 0 16 16" fill="#fff"><path d="M4 1l3 3-2 2c1 2 3 4 5 5l2-2 3 3-2 3C7 15 1 9 1 3z"/></svg><span>714-555-0182</span></div>
    <div class="info"><svg width="16" height="16" viewBox="0 0 16 16" fill="none" stroke="#fff" stroke-width="1.5"><rect x="1.5" y="3.5" width="13" height="9"/><path d="M1.5 3.5 8 9l6.5-5.5"/></svg><span>hello@ridgelineflameguard.example</span></div>
  </div>
  <div class="foot-col" style="left:880px">
    <h4>Get In Touch</h4>
    <div class="socials"><span></span><span></span><span></span></div>
  </div>
  <div class="copy">
    <span style="left:120px">Copyright © 2023. All Rights Reserved</span>
    <span style="left:700px">Privacy Policy</span>
    <span style="left:960px">Terms &amp; Condition</span>
  </div>
</footer>

</body>
</html>
```